ZELVO Ice Cream Logo & Packaging Project

We need a logo and ice cream packaging for our new company Zelvo.

The company is based in Port Amara, Westhaven, West Africa. It will be a large scale business, going national. For example the minimum order is 120.000 pieces of the small cup. Zelvo will produce and sell affordable frozen dairy products directly to consumers through a unique street vending system.

Your design will have great exposure.

The word ZELVO refers to anything or something which is WONDERFUL OR EXTRAORDINARY. ZELVO is something EXPLOSIVE. Also ZELVO refers to a shape, The ZELVO shape is round,just like an ICE CREAM BALL.

We thought the design could incorporate and exploding rays around an ice cream ball or cone. The market responds well to colours and visuals.

People may use the word ZELVO in this context :

1-A man who has a very nice STRONG and TONED,and full of MUSCLES body is a ZELVO
2 -A great EVENT,big HUGE CONCERT is a ZELVO
3 -A powerful and tasty ICE CREAM is a ZELVO.

There are several packagings to design. See attached documents for sizes, but the first task is the logo and the small cup.

The lid will be transparent plastic so you can see the ice cream, so we don't need the flavours on the label.

100-120ml tub Small cup sleeve and full lid

Required info includes :

Marlune Ice Cream Co, Brookvale, Port Amara, Westhaven.

Ingredients : sugar, glucose solids, milk, bean gum, natural flavour, colour, milk chocolate

Afterwards we will need packaging for :

1050ml oval tub sleeve and full lid

2120ml oval tub sleeve and lid full

standard ice cream cone sleeve.

standard ice lolly sleeve (note sleeve will be transparent)

trolley cart image 60cm wide x 60cm heigh approx

Target Market(s)

All ages and nationalities. The company is based in Port Amara, Westhaven, West Africa which is a 3rd world country. The market respond well to colours and visuals.

Industry/Entity Type

It Company

Font styles to use
Serif
Sans Serif

Requirements
Must have
• Marlune Ice Cream Co, Brookvale, Port Amara, Westhaven.
• Ingredients : sugar, glucose solids, milk, bean gum, natural flavour, colour, milk chocolate.
Nice to have
• The word ZELVO refers to anything or something which is WONDERFUL OR EXTRAORDINARY. ZELVO is something EXPLOSIVE. Also ZELVO refers to a shape, The ZELVO shape is round,just like an ICE CREAM BALL.
• We thought the design could incorporate and exploding rays around an ice cream ball or cone.

```html
<!DOCTYPE html>
<html lang="en">
<head>
<meta charset="utf-8">
<title>Zelvo Ice-Cream – Cup Sleeve Colourways</title>
<link rel="stylesheet" href="https://fonts.googleapis.com/css2?family=Josefin+Sans:wght@400;600;700&display=swap">
<style>
  :root {
    --page: #ffffff;
    --navy: #1f1d5c;

    --blue-ray: #1a3a94;
    --blue-light: #b8c8cc;
    --brick: #a84c48;
    --panel-brick: #a84a46;
    --cream-text: #f6ece6;

    --sage-ray: #c0c6b8;
    --lilac-ray: #8e8fab;
    --sage-title: #7f9e90;
    --mint: #94dcb8;
    --mint-text: #b9ecd2;

    --scoop: #f3e2c6;
    --cone: #d9924a;
  }

  * { box-sizing: border-box; margin: 0; padding: 0; }

  html, body {
    width: 1200px;
    height: 849px;
    overflow: hidden;
    background: var(--page);
  }

  .sheet {
    position: relative;
    width: 1200px;
    height: 849px;
    font-family: "Josefin Sans", sans-serif;
    text-transform: uppercase;
  }

  .sleeve {
    position: absolute;
    left: 186px;
    width: 828px;
    height: 252px;
    display: flex;
  }
  .sleeve--classic { top: 162px; }
  .sleeve--pastel { top: 434px; }

  .sleeve__front {
    position: relative;
    width: 598px;
    height: 100%;
    overflow: hidden;
  }

  .sleeve__rays {
    position: absolute;
    inset: 0;
  }
  .sleeve--classic .sleeve__rays {
    background: radial-gradient(circle at 50% 25%, var(--blue-light) 0%, var(--blue-ray) 55%, var(--blue-light) 100%);
  }
  .sleeve--pastel .sleeve__rays {
    background: radial-gradient(circle at 50% 25%, var(--sage-ray) 0%, var(--lilac-ray) 55%, var(--sage-ray) 100%);
  }

  .sleeve__cone-art {
    position: absolute;
    left: 238px;
    top: 42px;
    width: 80px;
    height: 110px;
    border-radius: 40px 40px 12px 12px;
    background: linear-gradient(180deg, var(--scoop) 0%, var(--scoop) 55%, var(--cone) 100%);
  }

  .sleeve__title {
    position: absolute;
    left: 0;
    right: 0;
    text-align: center;
    line-height: 1;
    font-weight: 700;
    padding-left: 4px;
  }
  .sleeve__brand {
    top: 152px;
    font-size: 50px;
    letter-spacing: 4px;
  }
  .sleeve__product {
    top: 202px;
    font-size: 34px;
    letter-spacing: 1px;
  }
  .sleeve--classic .sleeve__title { color: var(--brick); }
  .sleeve--pastel .sleeve__title { color: var(--sage-title); }

  .sleeve__volume {
    position: absolute;
    top: 239px;
    left: 0;
    right: 0;
    text-align: center;
    font-size: 12px;
    line-height: 12px;
    font-weight: 600;
    letter-spacing: 1px;
    color: var(--navy);
    padding-left: 12px;
  }

  .sleeve__back {
    position: relative;
    width: 230px;
    height: 100%;
    text-align: center;
  }
  .sleeve--classic .sleeve__back { background: var(--panel-brick); color: var(--cream-text); }
  .sleeve--pastel .sleeve__back { background: var(--mint); color: var(--mint-text); }

  .info__heading {
    position: absolute;
    left: 0; right: 0;
    font-size: 13px;
    line-height: 13px;
    font-weight: 600;
    letter-spacing: 1.2px;
    color: var(--navy);
  }
  .info__heading--brand { top: 11px; }
  .info__heading--ingredients { top: 70px; }

  .info__text {
    position: absolute;
    left: 4px; right: 4px;
    font-size: 10px;
    line-height: 12px;
    letter-spacing: 1.1px;
  }
  .info__text--tagline { top: 31px; }
  .info__text--ingredients { top: 91px; }
  .info__text--address { top: 229px; font-size: 8px; line-height: 10px; letter-spacing: 1px; }

  .sleeve__back-art {
    position: absolute;
    left: 90px;
    top: 132px;
    width: 48px;
    height: 82px;
    border-radius: 24px 24px 8px 8px;
    background: linear-gradient(180deg, var(--scoop) 0%, var(--scoop) 55%, var(--cone) 100%);
  }
</style>
</head>
<body>
<main class="sheet">

  <section class="sleeve sleeve--classic">
    <div class="sleeve__front">
      <div class="sleeve__rays" role="img" aria-label="Swirling burst of blue and pale grey-blue rays radiating from the cone"></div>
      <div class="sleeve__cone-art" role="img" aria-label="Illustration of a melting vanilla scoop on a waffle cone"></div>
      <div class="sleeve__title sleeve__brand">ZELVO</div>
      <div class="sleeve__title sleeve__product">ICE-CREAM</div>
      <div class="sleeve__volume">100ML</div>
    </div>
    <div class="sleeve__back">
      <h2 class="info__heading info__heading--brand">ZELVO:</h2>
      <p class="info__text info__text--tagline">Wonderful, extraordinary,<br>and explosive</p>
      <h2 class="info__heading info__heading--ingredients">Ingredients:</h2>
      <p class="info__text info__text--ingredients">Sugar, glucose solids, milk,<br>bean gum, natural flavour,<br>colour, milk chocolate</p>
      <div class="sleeve__back-art" role="img" aria-label="Small melting vanilla cone illustration"></div>
      <p class="info__text info__text--address">Marlune Ice Cream Co, Brookvale,<br>Port Amara, Westhaven.</p>
    </div>
  </section>

  <section class="sleeve sleeve--pastel">
    <div class="sleeve__front">
      <div class="sleeve__rays" role="img" aria-label="Swirling burst of sage and lilac rays radiating from the cone"></div>
      <div class="sleeve__cone-art" role="img" aria-label="Illustration of a melting vanilla scoop on a waffle cone"></div>
      <div class="sleeve__title sleeve__brand">ZELVO</div>
      <div class="sleeve__title sleeve__product">ICE-CREAM</div>
      <div class="sleeve__volume">100ML</div>
    </div>
    <div class="sleeve__back">
      <h2 class="info__heading info__heading--brand">ZELVO:</h2>
      <p class="info__text info__text--tagline">Wonderful, extraordinary,<br>and explosive</p>
      <h2 class="info__heading info__heading--ingredients">Ingredients:</h2>
      <p class="info__text info__text--ingredients">Sugar, glucose solids, milk,<br>bean gum, natural flavour,<br>colour, milk chocolate</p>
      <div class="sleeve__back-art" role="img" aria-label="Small melting vanilla cone illustration"></div>
      <p class="info__text info__text--address">Marlune Ice Cream Co, Brookvale,<br>Port Amara, Westhaven.</p>
    </div>
  </section>

</main>
</body>
</html>
```